Pell Hamlet Summer Party Invitation

We need an invitation to be designed for our annual summer party for Pell Hamlet in Chelsea, London. The area has a relaxed family atmosphere but is on the edge of the bustle of Chelsea. The committee has specified the following:

TO INCLUDE THE FOLLOWING INFORMATION - will it be the same two sided format as last year? Maybe the reverse can use your pale blue and your London skyline "logo"

Should the following, highlighted in blue, be very bold on the front of the invite? With the Dorrow & Co sales and lettings logo.
SUMMER PARTY 2016
Pell Hamlet Chelsea is holding a Summer Party to celebrate the Hamlet's 90th Birthday

Date: Saturday 18th June 2016
Time: 2.00pm to 5.00pm
Place: Wimbrel Lane South (the pedestrianised section off Hassock Street) MAP?

Open to all residents of Pell Hamlet and admittance is by invitation only.
Please keep this invitation safe and bring it with you on the day

Then more detail on the rear:

Pell Hamlet Chelsea
Formerly known as Falbrook Residents' Association of Pell Hamlet

Email: falbrookra@mailvane.co.uk
Website: falbrookra-demo.co.uk
OUR TYPEFACE IS ARIAL. The rest can be in any typeface but Arial is our "logo"

Dress code: red white and blue (or black ) as simple or elaborate as you like Live Music Children's entertainment and activities Food Drinks Tea and cakes

SPONSORS:
Dorrow & Co. Ensuring this is prominent as the main sponsor Gilded Otter
412 Blues club etc etc
Harrow Pike Studios
List to follow.............

Space needs to be left on the rear for sponsors details to be added. They would like something with an almost retro, traditional British feel.
Our Dorrow & Co logo attached and branding.

Also a flyer that association seemed to like.

I would suggest postcard (A6 sized) or maybe A5 at the biggest

Target Market(s)

Local Residents

Colors
ec1f27
ffffff
0355a3

Requirements
Must have
• Information on the description

```html
<!DOCTYPE html>
<html lang="en">
<head>
<meta charset="utf-8">
<title>Pell Hamlet Summer Party 2016 Invitation</title>
<link rel="stylesheet" href="https://fonts.googleapis.com/css2?family=Montserrat:wght@800&family=Cinzel:wght@600;700&family=Arimo:ital,wght@0,400;0,700;1,700&display=swap">
<style>
  :root {
    --stage: #000000;
    --navy-deep: #0f3f66;
    --navy-mid: #1c5f8c;
    --panel: #0b3477;
    --panel-edge: #1f5a4a;
    --pale-blue: #6ccbe6;
    --ice: #eaf8fc;
    --teal-shadow: #3d8fb0;
    --logo-teal: #2b7f9a;
    --gold: #f4ea6e;
    --rule: #6fb3cf;
    --ink: #2d3b45;
    --sponsor-tab: #1d6e86;
    --pink: #ec1f7a;
    --orange: #f47b20;
    --lime: #93c83e;
    --indigo: #2f3d8f;
    --red: #ec1f4a;
  }
  * { box-sizing: border-box; margin: 0; padding: 0; }
  html, body { width: 1187px; height: 1200px; overflow: hidden; background: var(--stage); }
  .invitation {
    position: absolute; left: 283px; top: 185px; width: 621px; height: 858px;
    background: radial-gradient(ellipse at 50% 30%, var(--navy-mid) 0%, var(--navy-deep) 85%);
    border: 1px solid var(--rule);
    overflow: hidden;
    font-family: "Arimo", Arial, sans-serif;
    color: #fff;
  }
  .abs { position: absolute; }
  .centered { left: 0; width: 100%; text-align: center; }
  .brand {
    top: 12px; font-family: "Arimo", Arial, sans-serif; font-weight: 700;
    font-size: 24px; letter-spacing: 1px; color: var(--logo-teal);
  }
  .headline {
    font-family: "Montserrat", sans-serif; font-weight: 800; color: var(--ice);
    line-height: 1; letter-spacing: 1px;
    text-shadow: 0 0 2px #fff, 2px 3px 0 var(--teal-shadow), 4px 6px 8px rgba(0,0,0,.55);
  }
  .headline-summer { top: 62px; left: 35px; font-size: 116px; }
  .headline-party { top: 165px; left: 104px; font-size: 116px; }
  .year { top: 219px; left: 503px; font-family: "Arimo", Arial, sans-serif; font-weight: 700; font-size: 36px; letter-spacing: -3px; }
  .year .d1 { color: var(--orange); }
  .year .d2 { color: var(--pink); }
  .year .d3 { color: var(--gold); }
  .year .d4 { color: var(--lime); }
  .details-panel {
    left: 74px; top: 295px; width: 473px; height: 135px;
    background: var(--panel); border: 6px solid var(--panel-edge); border-radius: 8px;
    box-shadow: 0 0 10px rgba(0,0,0,.4);
  }
  .announce {
    font-family: "Cinzel", serif; font-weight: 700; font-size: 16px; line-height: 17px;
    top: 14px; text-align: center; width: 100%;
  }
  .announce .highlight { color: var(--gold); }
  .panel-rule { left: 33px; width: 396px; top: 70px; border-top: 1px solid var(--rule); }
  .event-facts { top: 79px; width: 100%; text-align: center; font-size: 12.5px; line-height: 15.5px; }
  .event-facts b { color: var(--gold); }
  .admission { top: 449px; font-style: italic; font-weight: 700; font-size: 11.5px; line-height: 15px; }
  .association { top: 486px; font-family: "Cinzel", serif; font-weight: 700; font-size: 15.5px; line-height: 17px; color: var(--gold); }
  .rule { left: 67px; width: 486px; border-top: 1px solid var(--rule); }
  .tag {
    height: 26px; line-height: 26px; text-align: center; font-size: 14px; color: #fff;
  }
  .tag-music { left: 122px; top: 542px; width: 101px; background: var(--pink); }
  .tag-kids { left: 231px; top: 542px; width: 267px; background: var(--orange); }
  .tag-food { left: 122px; top: 578px; width: 101px; background: var(--lime); }
  .tag-drinks { left: 231px; top: 578px; width: 108px; background: var(--indigo); }
  .tag-tea { left: 350px; top: 578px; width: 148px; background: var(--red); }
  .dress-code { top: 627px; font-style: italic; font-weight: 700; font-size: 11.5px; }
  .skyline {
    left: 0; top: 655px; width: 100%; height: 56px;
    background: linear-gradient(to bottom, rgba(108,203,230,0) 0%, var(--pale-blue) 100%);
  }
  .footer { left: 0; top: 710px; width: 100%; height: 148px; background: var(--pale-blue); }
  .contact { top: 727px; font-size: 11.5px; color: var(--ink); }
  .sponsor-rule { top: 760px; border-top: 1px solid var(--ink); width: 207px; }
  .sponsor-tab {
    left: 229px; top: 753px; width: 162px; height: 16px; line-height: 16px;
    background: var(--sponsor-tab); color: var(--pale-blue); text-align: center;
    font-size: 11px; letter-spacing: 7px;
  }
  .sponsor { top: 805px; font-size: 16px; color: var(--ink); text-align: center; width: 170px; }
  .sponsor-divider { top: 793px; height: 40px; border-left: 1px solid var(--ink); }
</style>
</head>
<body>
  <main class="invitation">
    <div class="abs centered brand">Dorrow &amp; Co</div>

    <div class="abs headline headline-summer">SUMMER</div>
    <div class="abs headline headline-party">PARTY</div>
    <div class="abs year"><span class="d1">2</span><span class="d2">0</span><span class="d3">1</span><span class="d4">6</span></div>

    <section class="abs details-panel">
      <p class="abs announce">Pell Hamlet Chelsea is<br>holding a Summer Party to celebrate<br><span class="highlight">the Hamlet's 90th Birthday</span></p>
      <div class="abs panel-rule"></div>
      <p class="abs event-facts"><b>Date:</b> Saturday 18th June 2016 &nbsp;•&nbsp; <b>Time:</b> 2.00pm to 5.00pm<br><b>Place:</b> Wimbrel Lane South (the pedestrianised section off Hassock Street)</p>
    </section>

    <p class="abs centered admission">Open to all residents of Pell Hamlet and admittance is by invitation only.<br>Please keep this invitation safe and bring it with you on the day</p>
    <p class="abs centered association">Pell Hamlet Chelsea &nbsp;- Formerly known as<br>Falbrook Residents' Association of Pell Hamlet</p>

    <div class="abs rule" style="top:529px"></div>
    <div class="abs tag tag-music">Live Music</div>
    <div class="abs tag tag-kids">Children's entertainment and activities</div>
    <div class="abs tag tag-food">Food</div>
    <div class="abs tag tag-drinks">Drinks</div>
    <div class="abs tag tag-tea">Tea and cakes</div>
    <div class="abs rule" style="top:615px"></div>

    <p class="abs centered dress-code">Dress Code: Red White and Blue (or Black) as simple or elaborate as you like.</p>

    <div class="abs skyline" role="img" aria-label="City skyline silhouette with a big wheel, a domed cathedral, a towered bridge and a riverside dome"></div>
    <footer class="abs footer"></footer>

    <p class="abs centered contact">Email: falbrookra@mailvane.co.uk &nbsp;•&nbsp; Website: falbrookra-demo.co.uk</p>
    <div class="abs sponsor-rule" style="left:22px"></div>
    <div class="abs sponsor-rule" style="left:391px"></div>
    <div class="abs sponsor-tab">SPONSORS:</div>

    <p class="abs sponsor" style="left:47px">Gilded Otter</p>
    <div class="abs sponsor-divider" style="left:212px"></div>
    <p class="abs sponsor" style="left:206px">412 Blues club</p>
    <div class="abs sponsor-divider" style="left:372px"></div>
    <p class="abs sponsor" style="left:388px">Harrow Pike Studios</p>
  </main>
</body>
</html>
```